Serenqora: a Holistic Healing Company
Serenqora: Unlocking the Strengths for Balance Inside Each of Us
TO ALL DESIGNERS:
PLEASE BE SURE TO CHANGE THE WORD "PRESIDENT' TO "FOUNDER" (DO NOT ADD QUOTES)
ALSO, PLEASE ADD THE CELL NUMBER AS WELL AS THE TOLL FREE NUMBER.
THANK YOU!
PLEASE PROVIDE DESIGNS FOR LETTER HEADS AND ENVELOPES TOO. THANKYOU
THIS CONTEST IS FOR BOTH BUSINESS CARD DESIGN AND
STATIONARY DESIGN USING THE SERENQORA LOGO.

```html
<!DOCTYPE html>
<html lang="en">
<head>
<meta charset="utf-8">
<title>Serenqora Business Cards</title>
<link href="https://fonts.googleapis.com/css2?family=Cinzel:wght@500;600&family=Open+Sans:wght@400;700&family=Cormorant+Garamond:ital,wght@0,500;1,500&display=swap" rel="stylesheet">
<style>
  :root {
    --stage: #e9e4dc;
    --card-white: #ffffff;
    --card-black: #050505;
    --brand-blue: #2f6fc4;
    --brand-blue-dark: #1b3f8f;
    --brand-blue-light: #5fa3e8;
    --swoosh-grey: #9a9a9a;
    --text-dark: #333333;
    --text-light: #d8d8d8;
    --tagline-gold: #8a6a2e;
    --label: #3a3530;
  }
  * { box-sizing: border-box; margin: 0; padding: 0; }
  html, body { width: 1200px; height: 814px; overflow: hidden; }
  body { background: var(--stage); position: relative; font-family: "Open Sans", Arial, sans-serif; }

  .card {
    position: absolute; width: 510px; height: 292px; border-radius: 16px;
    overflow: hidden; box-shadow: 0 3px 8px rgba(0,0,0,.25);
  }
  .card--light { background: var(--card-white); color: var(--text-dark); }
  .card--dark { background: var(--card-black); color: var(--text-light); }
  .card--back { height: 252px; }

  .card-front-left { left: 67px; top: 43px; }
  .card-front-right { left: 619px; top: 43px; }
  .card-back-left { left: 67px; top: 492px; }
  .card-back-right { left: 619px; top: 492px; }

  .swoosh { position: absolute; inset: 0; }

  .brand { position: absolute; left: 22px; top: 38px; display: flex; align-items: center; gap: 10px; }
  .brand-dot { width: 16px; height: 16px; border-radius: 50%; background: var(--brand-blue); }
  .brand-name {
    font-family: "Cinzel", Georgia, serif; font-weight: 600; font-size: 30px;
    letter-spacing: 5px; color: var(--brand-blue);
  }
  .tagline {
    position: absolute; left: 24px; top: 86px; font-family: "Cormorant Garamond", Georgia, serif;
    font-style: italic; font-size: 13px; color: var(--tagline-gold);
  }
  .card--dark .tagline { color: #c9a86a; }

  .contact-list { position: absolute; left: 24px; top: 194px; list-style: none; font-size: 10.5px; line-height: 17px; }
  .contact-list li { display: flex; align-items: center; gap: 7px; }
  .contact-icon { width: 11px; height: 11px; flex: none; }

  .person { position: absolute; left: 300px; top: 196px; text-align: right; width: 150px; }
  .person-name { font-weight: 700; font-size: 16px; color: var(--brand-blue); }
  .person-role { font-size: 12px; }

  .back-brand { position: absolute; inset: 0; display: flex; align-items: center; justify-content: center; gap: 12px; }
  .back-brand .brand-name { font-size: 34px; }

  .label {
    position: absolute; width: 510px; text-align: center; font-family: "Cinzel", Georgia, serif;
    font-weight: 500; font-size: 22px; letter-spacing: 3px; color: var(--label);
  }
  .label-top-left { left: 67px; top: 364px; }
  .label-top-right { left: 619px; top: 364px; }
  .label-bottom-left { left: 67px; top: 764px; }
  .label-bottom-right { left: 619px; top: 764px; }
</style>
</head>
<body>

<svg width="0" height="0" style="position:absolute">
  <defs>
    <linearGradient id="blueBand" x1="0" y1="0" x2="1" y2="1">
      <stop offset="0" stop-color="#5fa3e8"/>
      <stop offset="0.6" stop-color="#2f6fc4"/>
      <stop offset="1" stop-color="#1b3f8f"/>
    </linearGradient>
    <linearGradient id="greyBand" x1="0" y1="0" x2="1" y2="0">
      <stop offset="0" stop-color="#cfcfcf"/>
      <stop offset="1" stop-color="#7d7d7d"/>
    </linearGradient>
    <symbol id="swooshShape" viewBox="0 0 510 292">
      <path d="M330,0 H510 V150 C490,80 430,25 330,0 Z" fill="url(#blueBand)"/>
      <path d="M510,118 C480,215 360,278 190,292 H270 C400,282 485,230 510,172 Z" fill="url(#greyBand)"/>
      <path d="M510,172 C485,230 400,282 270,292 H510 Z" fill="url(#blueBand)"/>
    </symbol>
    <symbol id="iconCircle" viewBox="0 0 12 12">
      <circle cx="6" cy="6" r="6" fill="#2f6fc4"/>
      <circle cx="6" cy="6" r="2" fill="#fff"/>
    </symbol>
  </defs>
</svg>

<section class="card card--light card-front-left">
  <svg class="swoosh" viewBox="0 0 510 292"><use href="#swooshShape"/></svg>
  <div class="brand"><span class="brand-dot"></span><span class="brand-name">SERENQORA</span></div>
  <p class="tagline">Unlocking the Strengths for Balance Inside Each of Us</p>
  <ul class="contact-list">
    <li><svg class="contact-icon"><use href="#iconCircle"/></svg>Maplewood, NY 10598</li>
    <li><svg class="contact-icon"><use href="#iconCircle"/></svg>877-555-0142</li>
    <li><svg class="contact-icon"><use href="#iconCircle"/></svg>917-555-0187</li>
    <li><svg class="contact-icon"><use href="#iconCircle"/></svg>info@serenqora.com</li>
    <li><svg class="contact-icon"><use href="#iconCircle"/></svg>www.serenqora.com</li>
  </ul>
  <div class="person"><p class="person-name">Dana Whitcombe</p><p class="person-role">Founder</p></div>
</section>

<section class="card card--dark card-front-right">
  <svg class="swoosh" viewBox="0 0 510 292"><use href="#swooshShape"/></svg>
  <div class="brand"><span class="brand-dot"></span><span class="brand-name">SERENQORA</span></div>
  <p class="tagline">Unlocking the Strengths for Balance Inside Each of Us</p>
  <ul class="contact-list">
    <li><svg class="contact-icon"><use href="#iconCircle"/></svg>Maplewood, NY 10598</li>
    <li><svg class="contact-icon"><use href="#iconCircle"/></svg>877-555-0142</li>
    <li><svg class="contact-icon"><use href="#iconCircle"/></svg>917-555-0187</li>
    <li><svg class="contact-icon"><use href="#iconCircle"/></svg>info@serenqora.com</li>
    <li><svg class="contact-icon"><use href="#iconCircle"/></svg>www.serenqora.com</li>
  </ul>
  <div class="person"><p class="person-name">Dana Whitcombe</p><p class="person-role">Founder</p></div>
</section>

<p class="label label-top-left">Business Card Front</p>
<p class="label label-top-right">Business Card Front</p>

<section class="card card--light card--back card-back-left">
  <div class="back-brand"><span class="brand-dot"></span><span class="brand-name">SERENQORA</span></div>
</section>

<section class="card card--dark card--back card-back-right">
  <div class="back-brand"><span class="brand-dot"></span><span class="brand-name">SERENQORA</span></div>
</section>

<p class="label label-bottom-left">Business Card Back</p>
<p class="label label-bottom-right">Business Card Back</p>

</body>
</html>
```